School Communication Email Template

Looking for a designer to create a couple simple email templates that are matching our brand colors and feel. Attached is the default email template that is currently being sent out. Company details can be shared upon request.

Template is to be used within the booking tool we use (snapshot below) and gmail. Template code is in HTML (see screenshot below).
Updates

Template code for website should be in HTML. Sorry if that created confusion.

Target Market(s)

Parents of kids enrolled in our classes

Industry/Entity Type

Kids sport classes

Font styles to use
Serif

Colors
0054AA
0677BA
7BADD7
CADEEF
E8F1F8
FFF300
FFF600
FEFA6F
FFFEC7
FFFEE8

Requirements
Must have
• Consistency with company brand/colors
Nice to have
• Flexibility to be adjusted as needed

```html
<!DOCTYPE html>
<html lang="en">
<head>
<meta charset="utf-8">
<title>Booking Confirmation Email</title>
<link rel="stylesheet" href="https://fonts.googleapis.com/css2?family=Roboto:wght@400;500&display=swap">
<style>
  :root {
    --brand-blue: #233b8e;
    --brand-gold: #e8c11f;
    --page-bg: #ffffff;
    --text-dark: #1f1f1f;
    --text-field: #5a5a5a;
    --field-bg: #ffffff;
    --field-shadow: rgba(0, 0, 0, 0.12);
  }
  * { box-sizing: border-box; margin: 0; padding: 0; }
  html, body {
    width: 1200px;
    height: 2388px;
    overflow: hidden;
    background: var(--page-bg);
    font-family: "Roboto", Arial, sans-serif;
  }
  .email {
    position: relative;
    width: 1200px;
    height: 2388px;
  }
  .brand {
    position: absolute;
    left: 0;
    top: 118px;
    width: 1200px;
    display: flex;
    justify-content: center;
    align-items: center;
    gap: 16px;
  }
  .brand-dot {
    width: 34px;
    height: 34px;
    border-radius: 50%;
    background: var(--brand-gold);
  }
  .brand-name {
    font-size: 46px;
    font-weight: 500;
    color: var(--brand-blue);
    line-height: 60px;
  }
  .heading {
    position: absolute;
    left: 96px;
    color: var(--brand-blue);
    font-weight: 500;
    font-size: 46px;
    line-height: 1;
  }
  .heading--greeting { top: 420px; }
  .heading--booking { top: 616px; }
  .label {
    position: absolute;
    left: 96px;
    font-size: 31px;
    color: var(--text-dark);
    line-height: 1;
  }
  .field {
    position: absolute;
    height: 111px;
    background: var(--field-bg);
    border-radius: 12px;
    box-shadow: 0 3px 18px var(--field-shadow);
    display: flex;
    align-items: center;
    padding-left: 40px;
    font-size: 23px;
    color: var(--text-field);
  }
  .field--wide { left: 96px; width: 869px; }
  .field--half-left { left: 96px; width: 423px; padding-left: 46px; }
  .field--half-right { left: 546px; width: 422px; padding-left: 45px; }
  .field--greet-first { left: 247px; top: 387px; width: 422px; }
  .field--greet-last { left: 696px; top: 387px; width: 422px; }
  .footer {
    position: absolute;
    left: 0;
    bottom: 0;
    width: 1200px;
    height: 129px;
    background: var(--brand-gold);
    display: flex;
    justify-content: center;
    align-items: center;
    font-size: 24px;
    color: var(--text-dark);
  }
  .footer-sep { margin: 0 24px; }
</style>
</head>
<body>
<div class="email">
  <header class="brand">
    <span class="brand-dot"></span>
    <span class="brand-name">Brightstar Sports</span>
  </header>

  <h1 class="heading heading--greeting">Dear</h1>
  <div class="field field--greet-first">Maya</div>
  <div class="field field--greet-last">Daniel Reed</div>

  <h2 class="heading heading--booking">Booking</h2>

  <div class="label" style="top:728px">Student</div>
  <div class="field field--half-left" style="top:789px">Student First Name</div>
  <div class="field field--half-right" style="top:789px">Student Last Name</div>

  <div class="label" style="top:948px">Appointment</div>
  <div class="field field--wide" style="top:1005px">Lorem ipsum dolor sit</div>

  <div class="label" style="top:1152px">Service</div>
  <div class="field field--wide" style="top:1209px">Parents of their children to school</div>

  <div class="label" style="top:1362px">Start date</div>
  <div class="field field--wide" style="top:1419px">15 - 02 - 2023</div>

  <div class="label" style="top:1563px">End date</div>
  <div class="field field--wide" style="top:1620px">18 - 02 - 2023</div>

  <div class="label" style="top:1773px">Start time</div>
  <div class="field field--wide" style="top:1830px">8.00 am</div>

  <div class="label" style="top:1981px">End time</div>
  <div class="field field--wide" style="top:2038px">5.00 pm</div>

  <footer class="footer">
    <span>©Copyrights 2023 Company Name</span>
    <span class="footer-sep">|</span>
    <span>All Rights Reserved</span>
  </footer>
</div>
</body>
</html>
```